Velqor5 Business Card - Health

Velqor5 maximizes value from the health data of its clients, including doctors, HMOs, and patients. I have attached the Velqor5 logo as an ai and eps file.
Target Market(s)
Health, HMO, Healthcare, Data, Big Data, Data Analytics
Industry/Entity Type
Business
Requirements
Must have
- At least one side should have some white on it so that we can write on it.

```html
<!DOCTYPE html>
<html lang="en">
<head>
<meta charset="utf-8">
<title>Velqor5 Business Card</title>
<link rel="stylesheet" href="https://fonts.googleapis.com/css2?family=Questrial&family=Open+Sans:wght@400;600;700&display=swap">
<style>
  :root {
    --backdrop: #8a8a8a;
    --card-black: #000000;
    --band-dark: #141414;
    --brand-blue: #1e88e5;
    --brand-blue-light: #3fa2f3;
    --stripe-white: #f4f4f4;
    --write-white: #ffffff;
    --text-white: #ffffff;
    --text-soft: #e6e6e6;
  }
  * { box-sizing: border-box; margin: 0; padding: 0; }
  html, body {
    width: 1200px; height: 900px; overflow: hidden;
    background: var(--backdrop);
  }
  .sheet {
    position: relative; width: 1200px; height: 900px;
    display: flex; flex-direction: column; align-items: center; justify-content: center; gap: 44px;
  }
  .card {
    position: relative; width: 700px; height: 400px;
    background: var(--card-black); overflow: hidden;
    box-shadow: 0 6px 18px rgba(0,0,0,0.35);
  }
  .stripe { position: absolute; left: 0; width: 100%; }
  .stripe--white { background: var(--stripe-white); }
  .stripe--blue { background: linear-gradient(180deg, var(--brand-blue-light), var(--brand-blue)); }
  .write-area { background: var(--write-white); }

  /* Front side */
  .front .wordmark {
    position: absolute; right: 56px; top: 190px;
    font-family: "Questrial", sans-serif; font-size: 96px; line-height: 1;
    color: var(--text-white); letter-spacing: 1px;
  }

  /* Back side */
  .brand {
    position: absolute; left: 44px; top: 84px;
    display: flex; align-items: center; gap: 22px;
  }
  .brand__dot {
    width: 74px; height: 74px; border-radius: 50%; background: var(--brand-blue);
  }
  .brand__name {
    font-family: "Questrial", sans-serif; font-size: 76px; line-height: 1;
    color: var(--text-soft);
  }
  .person {
    position: absolute; right: 36px; top: 58px; text-align: right;
    font-family: "Open Sans", sans-serif;
  }
  .person__name { color: var(--brand-blue); font-weight: 700; font-size: 17px; letter-spacing: 0.5px; }
  .person__title { color: var(--text-white); font-size: 16px; margin-top: 2px; }

  .info-band {
    position: absolute; left: 0; top: 222px; width: 100%; height: 100px;
    background: var(--band-dark);
    display: flex; justify-content: space-between; align-items: center;
    padding: 0 36px 0 44px;
    font-family: "Open Sans", sans-serif; font-size: 15px; color: var(--text-white);
  }
  .info-group { display: flex; flex-direction: column; gap: 6px; }
  .info-line { display: flex; align-items: flex-start; gap: 8px; line-height: 1.35; }
  .info-line svg { flex: none; width: 13px; height: 13px; margin-top: 3px; fill: var(--brand-blue); }
</style>
</head>
<body>
<main class="sheet">

  <section class="card front" aria-label="Card front">
    <div class="wordmark">Velqor5</div>
    <div class="stripe stripe--white" style="top:308px;height:12px"></div>
    <div class="stripe stripe--blue" style="top:320px;height:58px"></div>
    <div class="stripe stripe--white" style="top:378px;height:10px"></div>
    <div class="stripe stripe--blue" style="top:388px;height:12px"></div>
  </section>

  <section class="card back" aria-label="Card back">
    <div class="brand">
      <span class="brand__dot"></span>
      <span class="brand__name">Velqor5</span>
    </div>
    <div class="person">
      <p class="person__name">MARCUS ELLERY</p>
      <p class="person__title">Managing Director</p>
    </div>

    <div class="info-band">
      <div class="info-group">
        <p class="info-line">
          <svg viewBox="0 0 12 12" aria-hidden="true"><path d="M6 0a4 4 0 0 0-4 4c0 3 4 8 4 8s4-5 4-8a4 4 0 0 0-4-4zm0 5.5A1.5 1.5 0 1 1 6 2.5a1.5 1.5 0 0 1 0 3z"/></svg>
          <span>1234, Address Goes Here,<br>Country Name, 123456</span>
        </p>
      </div>
      <div class="info-group">
        <p class="info-line">
          <svg viewBox="0 0 12 12" aria-hidden="true"><path d="M1 3c0-1.5 2-2 5-2s5 .5 5 2v1H8V3H4v1H1zM2 5h8l1 6H1z"/></svg>
          <span>123.456.7890</span>
        </p>
        <p class="info-line">
          <svg viewBox="0 0 12 12" aria-hidden="true"><path d="M3 0h6v3H3zM1 4h10v6H9v2H3v-2H1zm3 4v3h4V8z"/></svg>
          <span>123.456.7890</span>
        </p>
      </div>
      <div class="info-group">
        <p class="info-line">
          <svg viewBox="0 0 12 12" aria-hidden="true"><path d="M0 2h12v8H0zm1 1v.3l5 3.5 5-3.5V3z"/></svg>
          <span>hello@velqor5.com</span>
        </p>
        <p class="info-line">
          <svg viewBox="0 0 12 12" aria-hidden="true"><path d="M5 7l2-2M4.5 5.5 3 7a2 2 0 0 0 2 2l1.5-1.5M7.5 6.5 9 5a2 2 0 0 0-2-2L5.5 4.5" stroke="#1e88e5" stroke-width="1.4" fill="none" stroke-linecap="round"/></svg>
          <span>www.velqor5.com</span>
        </p>
      </div>
    </div>

    <div class="stripe stripe--blue" style="top:322px;height:8px"></div>
    <div class="stripe write-area" style="top:330px;height:56px"></div>
    <div class="stripe stripe--blue" style="top:386px;height:14px"></div>
  </section>

</main>
</body>
</html>
```